Thai Massage Poster Replication. Project will be awarded to design that replicates picture closest. We recommend to use tracing paper to get outline. Please see attached files for picture that is desired to be replicated.

Try to add Thai herbs and herbal compress into the background if possible. See attached images.

Industry/Entity Type

Massage

```html
<!DOCTYPE html>
<html lang="en">
<head>
<meta charset="utf-8">
<title>Thai Massage Poster</title>
<link rel="stylesheet" href="https://fonts.googleapis.com/css2?family=Arimo:wght@700&family=Bubblegum+Sans&family=Chewy&family=Dancing+Script:wght@600&family=Delius&display=swap">
<style>
  :root {
    --page: #ffffff;
    --glow: #f7b27a;
    --frame: #3b1812;
    --field: #4b4429;
    --field-light: #5a5233;
    --cream: #f8e6a6;
    --orange: #f6a823;
    --red: #ee1111;
    --white: #ffffff;
    --lime: #d8f000;
    --outline: #2a1208;
    --ornament: #6b5a44;
    --photo-skin: #b48a5c;
    --photo-gold: #a8791e;
    --photo-green: #4f7a3a;
    --compress: #e8e8e6;
  }
  * { margin: 0; padding: 0; box-sizing: border-box; }
  html, body { width: 1000px; height: 1200px; overflow: hidden; background: var(--page); }
  .canvas { position: relative; width: 1000px; height: 1200px; }
  .poster {
    position: absolute; left: 95px; top: 36px; width: 800px; height: 1130px;
    background: var(--frame);
    box-shadow: 0 0 40px 18px var(--glow);
  }
  .poster-field {
    position: absolute; left: 22px; top: 22px; right: 22px; bottom: 22px;
    background: radial-gradient(ellipse at 50% 40%, var(--field-light), var(--field) 70%);
  }
  .corner-ornament {
    position: absolute; width: 170px; height: 150px; opacity: 0.6;
  }
  .corner-ornament.tl { left: 0; top: 0; background: radial-gradient(ellipse at 0 0, var(--ornament), transparent 70%); }
  .corner-ornament.tr { right: 0; top: 0; background: radial-gradient(ellipse at 100% 0, var(--ornament), transparent 70%); }
  .corner-ornament.bl { left: 0; bottom: 0; background: radial-gradient(ellipse at 0 100%, var(--ornament), transparent 70%); }
  .corner-ornament.br { right: 0; bottom: 0; background: radial-gradient(ellipse at 100% 100%, var(--ornament), transparent 70%); }
  .title-thai {
    position: absolute; left: 172px; top: 70px;
    font-family: "Dancing Script", cursive; font-size: 250px; line-height: 1;
    letter-spacing: 4px; color: var(--cream);
  }
  .herbal-compress {
    position: absolute; left: 608px; top: 150px; width: 158px; height: 180px;
    background: radial-gradient(ellipse at 45% 70%, #ffffff, var(--compress) 60%, #bdbdba);
    border-radius: 45% 45% 50% 50%;
  }
  .title-massage {
    position: absolute; left: 272px; top: 300px;
    font-family: "Delius", sans-serif; font-size: 138px; line-height: 1;
    color: var(--orange);
  }
  .therapist-photo {
    position: absolute; left: 115px; top: 455px; width: 338px; height: 688px;
    background: linear-gradient(180deg, var(--photo-skin) 0%, var(--photo-skin) 22%, var(--photo-gold) 30%, #7a5616 75%, #3a2a14 100%);
    border-radius: 120px 120px 20px 20px;
  }
  .price {
    position: absolute; left: 455px; top: 500px; width: 350px; text-align: center;
    font-family: "Arimo", sans-serif; font-weight: 700; color: var(--red);
    -webkit-text-stroke: 7px var(--white); paint-order: stroke fill;
  }
  .price-amount { display: block; font-size: 200px; line-height: 1; letter-spacing: -2px; }
  .price-unit { display: block; font-size: 90px; line-height: 1; margin-left: 160px; margin-top: -20px; }
  .herbs-photo {
    position: absolute; left: 410px; top: 735px; width: 440px; height: 230px;
    background: radial-gradient(ellipse at 50% 55%, var(--photo-green), #3a5a2a 55%, transparent 75%);
  }
  .opening-days, .opening-hours {
    position: absolute; left: 95px; width: 800px; text-align: center;
    font-family: "Bubblegum Sans", "Chewy", sans-serif; line-height: 1;
    -webkit-text-stroke: 8px var(--outline); paint-order: stroke fill;
  }
  .opening-days { top: 1005px; font-size: 60px; color: var(--lime); transform: skewX(-6deg); }
  .opening-hours { top: 1075px; font-size: 58px; color: var(--white); transform: skewX(-6deg); }
</style>
</head>
<body>
<div class="canvas">
  <div class="poster">
    <div class="poster-field"></div>
    <div class="corner-ornament tl" role="img" aria-label="Thai scroll ornament"></div>
    <div class="corner-ornament tr" role="img" aria-label="Thai scroll ornament"></div>
    <div class="corner-ornament bl" role="img" aria-label="Thai scroll ornament"></div>
    <div class="corner-ornament br" role="img" aria-label="Thai scroll ornament"></div>
  </div>
  <div class="title-thai">Thai</div>
  <div class="herbal-compress" role="img" aria-label="White herbal compress ball"></div>
  <div class="title-massage">Massage</div>
  <div class="therapist-photo" role="img" aria-label="Photo of a smiling therapist in a gold silk dress giving a wai greeting"></div>
  <div class="herbs-photo" role="img" aria-label="Photo of a stone mortar and pestle with fresh Thai herbs and a small oil bottle"></div>
  <div class="price"><span class="price-amount">$40</span><span class="price-unit">HR</span></div>
  <div class="opening-days">Open 7 Days a Week</div>
  <div class="opening-hours">10am - 9pm</div>
</div>
</body>
</html>
```